Website re-design for a Gardening - Vegetable Growing -Compost Ecommerce site

We need a "green & organic" looking web design for The Loam Barrow website re-design. The website sells garden and landscape supplies, and specialises in composites and vegetable growing products which are sold nationwide throughout the UK.

This project is for a homepage & content page design which can be used as a template to create other pages through the site, ideally with css and coding for a joomla template.

Our customer base is made up of gardeners & vegetable growers. The site is an ecommerce site run on Joomla CMS, we will be converting the design into a joomla template.

The Home page will contain information and attractive garden & vegetable growing images linking to information and product / shop category pages.

Current site: www.theloambarrow.co.uk

Sites I like the look of :

http://fernquillplot.com/index.php
http://albumpage.stationnine.com
http://www.squirmydelvers.co.uk/
http://www.hamletcreamery.co.uk
Updates

Hi Guys! Feel free to use different colour schemes from the three colours i have suggested in the brief. I am open to any suggestions, but a modern look and feel is preferred.

Target Market(s)

Home owners, vegetable growers and keen gardeners

Industry/Entity Type

Landscape

Coding

Coded - Design and coding required

Font styles to use
Sans Serif

Colors
9bcb3c
faa54b
fece3e

Requirements
Must have
• a white main content background

```html
<!DOCTYPE html>
<html lang="en">
<head>
<meta charset="utf-8">
<title>The Loam Barrow – Home</title>
<link rel="stylesheet" href="https://fonts.googleapis.com/css2?family=Open+Sans:wght@400;600&family=Roboto:wght@400;500&display=swap">
<style>
:root{
  --green:#8dbb2e;
  --green-dark:#6f9a1c;
  --green-light:#9bcb3c;
  --orange:#f39a33;
  --orange-light:#faa54b;
  --yellow:#fece3e;
  --ink:#1f1f1f;
  --text:#555;
  --muted:#777;
  --line:#d8d8d8;
  --nav:#1a1a1a;
  --foot:#f2f2f2;
  --foot-dark:#222;
}
*{box-sizing:border-box;margin:0;padding:0}
html,body{width:986px;height:1200px;overflow:hidden;background:#fff}
body{position:relative;font-family:"Open Sans",Arial,sans-serif;color:var(--text)}
.abs{position:absolute}

/* header */
.topline{left:0;top:0;width:986px;height:2px;background:var(--orange-light)}
.header{left:0;top:2px;width:986px;height:72px;background:linear-gradient(90deg,#e4e2dc,#eceae6 40%,#dcd8cf 70%,#e6e4df)}
.brand{left:148px;top:22px;display:flex;align-items:center;gap:8px}
.brand-dot{width:24px;height:24px;border-radius:50%;background:var(--yellow)}
.brand-name{font-family:"Roboto",sans-serif;font-size:23px;font-weight:500;color:var(--green)}
.cart{left:734px;top:28px;width:104px;height:30px;background:var(--orange);border-radius:2px;color:#fff;font-size:10px;display:flex;align-items:center;justify-content:center;gap:6px}

/* nav */
.nav{left:0;top:74px;width:986px;height:38px;background:linear-gradient(#262626,#111)}
.nav a{position:absolute;top:0;height:38px;line-height:38px;color:#fff;font-size:10px;text-decoration:none}
.nav .active{left:149px;width:83px;background:var(--green);text-align:center}

/* slider */
.slider{left:148px;top:122px;width:690px;height:376px;border:1px solid var(--line);background:#fff;box-shadow:0 10px 8px -8px rgba(0,0,0,.45)}
.slide{left:154px;top:127px;width:680px;height:366px;background:linear-gradient(180deg,#6aa32e 0%,#8cc240 30%,#4d6b2a 55%,#2c2018 75%,#1d1510 100%)}
.caption{left:416px;top:388px;width:418px;height:68px;background:rgba(0,0,0,.55);color:#fff;font-size:18px;line-height:21px;padding:10px 0 0 34px}
.dot{top:473px;width:9px;height:9px;border-radius:50%;background:#fff}
.dot.off{background:transparent;border:2px solid #fff}

/* cards */
.card{top:530px;width:162px;height:260px;background:#f4f4f4;border:1px solid var(--line);box-shadow:0 8px 6px -6px rgba(0,0,0,.45)}
.card h3{position:absolute;left:16px;top:14px;width:140px;height:34px;display:flex;align-items:center;font-family:"Roboto",sans-serif;font-weight:400;font-size:12px;line-height:17px;color:var(--ink)}
.card .photo{position:absolute;left:14px;top:46px;width:134px;height:82px}
.card p{position:absolute;left:14px;top:134px;width:138px;font-size:9px;line-height:17px;color:var(--muted)}
.card p span{color:var(--orange-light)}
.card .btn{position:absolute;left:14px;top:209px;width:88px;height:33px;background:linear-gradient(var(--green-light),var(--green-dark));color:#fff;font-size:10px;display:flex;align-items:center;justify-content:center;border-radius:2px}

/* welcome */
h2{font-family:"Roboto",sans-serif;font-weight:400;font-size:18px;color:var(--ink)}
.welcome{left:148px;top:822px;width:452px}
.welcome p{font-size:9.5px;line-height:17px;margin-top:4px;color:#444}
.welcome p+p{margin-top:12px}
.products{left:618px;top:822px}
.products ul{list-style:none;margin-top:6px}
.products li{display:flex;align-items:center;gap:7px;font-size:9.5px;color:#333;height:21px}
.products li svg{flex:none}

/* features */
.feature{top:974px;width:160px;height:50px}
.feature .icon{position:absolute;left:0;top:0;width:48px;height:48px;border-radius:50%;background:var(--orange);box-shadow:0 2px 3px rgba(0,0,0,.25);display:flex;align-items:center;justify-content:center}
.feature h4{position:absolute;left:54px;top:0;font-family:"Roboto",sans-serif;font-weight:400;font-size:13px;color:var(--green-light)}
.feature p{position:absolute;left:54px;top:18px;width:104px;font-size:9px;line-height:14px;color:#444}

/* footer */
.footer{left:0;top:1046px;width:986px;height:109px;background:var(--foot)}
.footer h5{position:absolute;font-family:"Roboto",sans-serif;font-weight:400;font-size:13px;color:var(--ink)}
.footer .lnk{position:absolute;font-size:9px;color:var(--muted)}
.soc{position:absolute;width:10px;height:10px;background:#bbb}
.email{left:541px;top:1084px;width:143px;height:29px;border:1px solid #ccc;background:#fff;font-size:9px;color:#999;padding:8px 0 0 7px}
.subscribe{left:541px;top:1118px;width:85px;height:24px;background:var(--green);color:#fff;font-size:10px;font-weight:600;display:flex;align-items:center;justify-content:center;border-radius:2px}
.secure{left:720px;top:1086px;display:flex;align-items:center;gap:8px}
.secure-box{width:26px;height:26px;background:#7aa83a;border-radius:3px}
.secure-text{font-size:8px;color:#888;line-height:10px}
.secure-text b{display:block;font-family:"Open Sans",sans-serif;font-weight:400;font-size:18px;line-height:20px;color:#666}
.bottom{left:0;top:1155px;width:986px;height:45px;background:var(--foot-dark);color:#ddd;font-size:9px;text-align:center;line-height:45px}
</style>
</head>
<body>

<div class="abs topline"></div>
<div class="abs header" role="img" aria-label="Faded background of garden soil and leaves"></div>
<div class="abs brand"><span class="brand-dot"></span><span class="brand-name">The Loam Barrow</span></div>
<div class="abs cart">
  <svg width="12" height="10" viewBox="0 0 12 10"><path d="M1 3h10l-1.5 6h-7z M3.5 3 6 0.5 8.5 3" fill="none" stroke="#fff" stroke-width="1.3"/></svg>
  MY CART
</div>

<nav class="abs nav">
  <a class="active">HOME</a>
  <a style="left:246px">PRODUCTS</a>
  <a style="left:338px">ABOUT US</a>
  <a style="left:427px">WHAT WE DO</a>
  <a style="left:531px">GARDEN GURU</a>
  <a style="left:642px">BULK LOADS</a>
  <a style="left:742px">CONTACT US</a>
</nav>

<div class="abs slider"></div>
<div class="abs slide" role="img" aria-label="Carrots and radishes growing in dark soil"></div>
<div class="abs caption">Huge Range from Multi Purpose to Specialist Composts</div>
<span class="abs dot" style="left:473px"></span>
<span class="abs dot off" style="left:488px"></span>
<span class="abs dot" style="left:504px"></span>

<div class="abs card" style="left:148px">
  <h3>BUY COMPOST ONLINE</h3>
  <div class="photo" role="img" aria-label="Hands holding fresh compost" style="background:linear-gradient(135deg,#3a2c22,#2a1f18 50%,#c9a48a)"></div>
  <p>Buy compost and manure online in bags or 1m3 bulk bags online as well as many other garden...<span>(READ MORE)</span></p>
  <div class="btn">BULK LOADS</div>
</div>
<div class="abs card" style="left:324px">
  <h3>MANURE SUPPLIERS</h3>
  <div class="photo" role="img" aria-label="Manure being tipped from a spreader" style="background:linear-gradient(135deg,#a99a8c,#6b4a35 50%,#cfc9c2)"></div>
  <p>We supply, well-rotted, shred-ded horse manure which is collected from racing stables where the...<span>(READ MORE)</span></p>
  <div class="btn">BUY NOW</div>
</div>
<div class="abs card" style="left:500px">
  <h3>ORGANIC COMPOST<br>&nbsp;- PAS100</h3>
  <div class="photo" role="img" aria-label="Heap of organic compost in a yard" style="background:linear-gradient(180deg,#8a8274,#3a2e25 35%,#2a211b)"></div>
  <p>We specialise in the supply of peat free organic PAS100 com-post, a quality product made from recycled...<span>(READ MORE)</span></p>
  <div class="btn">BULK LOADS</div>
</div>
<div class="abs card" style="left:677px">
  <h3>BULK LOADS OF TOPSOIL &amp; BARK</h3>
  <div class="photo" role="img" aria-label="Large pile of topsoil with screening machinery" style="background:linear-gradient(180deg,#b7b0a2,#6b5a48 40%,#3e3027)"></div>
  <p>As well as bulk loads of compost we supply bulk loads of topsoil, bark and woodchip in various...<span>(READ MORE)</span></p>
  <div class="btn">BULK LOADS</div>
</div>

<section class="abs welcome">
  <h2>Welcome To The Loam Barrow</h2>
  <p>We've got all the compost, topsoil and garden supplies you'll need to get your garden in shape this year! Whether you just need some compost to top up your flower beds or want to start growing your own fruit and veg, we have everything you'll need and much more!</p>
  <p>As the UK's leading supplier, we have an extensive range of growing media as well as many other garden products such as organic compost, vegetable growing kits and baby vegetable seedlings!</p>
</section>

<section class="abs products">
  <h2>Our Products</h2>
  <ul>
    <li><svg width="11" height="11" viewBox="0 0 11 11"><rect x=".5" y=".5" width="10" height="10" fill="#fff" stroke="#aaa"/><path d="M2.5 5.5l2 2 4-5" fill="none" stroke="#6f9a1c" stroke-width="1.3"/></svg>Organic Compost Bulk Bag</li>
    <li><svg width="11" height="11" viewBox="0 0 11 11"><rect x=".5" y=".5" width="10" height="10" fill="#fff" stroke="#aaa"/><path d="M2.5 5.5l2 2 4-5" fill="none" stroke="#6f9a1c" stroke-width="1.3"/></svg>Children's Veg Garden</li>
    <li><svg width="11" height="11" viewBox="0 0 11 11"><rect x=".5" y=".5" width="10" height="10" fill="#fff" stroke="#aaa"/><path d="M2.5 5.5l2 2 4-5" fill="none" stroke="#6f9a1c" stroke-width="1.3"/></svg>Mushroom Compost</li>
    <li><svg width="11" height="11" viewBox="0 0 11 11"><rect x=".5" y=".5" width="10" height="10" fill="#fff" stroke="#aaa"/><path d="M2.5 5.5l2 2 4-5" fill="none" stroke="#6f9a1c" stroke-width="1.3"/></svg>Vegetable Blend Topsoil</li>
    <li><svg width="11" height="11" viewBox="0 0 11 11"><rect x=".5" y=".5" width="10" height="10" fill="#fff" stroke="#aaa"/><path d="M2.5 5.5l2 2 4-5" fill="none" stroke="#6f9a1c" stroke-width="1.3"/></svg>Border Blend Topsoil</li>
  </ul>
</section>

<div class="abs feature" style="left:148px">
  <div class="icon"><svg width="20" height="22" viewBox="0 0 20 22"><path d="M10 1 18 4v6c0 5-3.5 9-8 11C5.5 19 2 15 2 10V4z" fill="none" stroke="#fff" stroke-width="1.8"/><path d="M6 11l3 3 5-6" fill="none" stroke="#fff" stroke-width="1.8"/></svg></div>
  <h4>Great Value</h4><p>Lorem ipsum dolor sit amet, conse ctetuer</p>
</div>
<div class="abs feature" style="left:324px">
  <div class="icon"><svg width="22" height="22" viewBox="0 0 22 22"><path d="M3 3l16 16M19 3 3 19" stroke="#fff" stroke-width="3" stroke-linecap="round"/></svg></div>
  <h4>Quality Service</h4><p>Lorem ipsum dolor sit amet, conse ctetuer</p>
</div>
<div class="abs feature" style="left:501px">
  <div class="icon"><svg width="24" height="18" viewBox="0 0 24 18"><rect x="1" y="3" width="13" height="10" fill="#fff"/><path d="M14 6h5l4 4v3h-9z" fill="#fff"/><circle cx="6" cy="15" r="2.3" fill="#fff" stroke="#f39a33"/><circle cx="18" cy="15" r="2.3" fill="#fff" stroke="#f39a33"/></svg></div>
  <h4>Fast Delivery</h4><p>Lorem ipsum dolor sit amet, conse ctetuer</p>
</div>
<div class="abs feature" style="left:677px">
  <div class="icon"><svg width="20" height="20" viewBox="0 0 20 20"><rect x="1" y="8" width="4" height="10" fill="#fff"/><path d="M7 8l4-6c1.5 0 2 1 1.5 2.5L12 8h5c1 0 2 1 1.6 2.2l-2 6.3c-.3.9-1 1.5-2 1.5H7z" fill="#fff"/></svg></div>
  <h4>Finest Products</h4><p>Lorem ipsum dolor sit amet, conse ctetuer</p>
</div>

<footer class="abs footer">
  <h5 style="left:148px;top:16px">Information</h5>
  <span class="lnk" style="left:148px;top:40px">Special Offers</span>
  <span class="lnk" style="left:240px;top:40px">Privacy Policy</span>
  <span class="lnk" style="left:148px;top:62px">Events</span>
  <span class="lnk" style="left:240px;top:62px">Sitemap</span>
  <span class="lnk" style="left:148px;top:84px">Latest Products</span>

  <h5 style="left:329px;top:16px">Support</h5>
  <span class="lnk" style="left:329px;top:40px">Live Chat</span>
  <span class="lnk" style="left:329px;top:62px">Send Mail</span>
  <span class="lnk" style="left:329px;top:84px">FAQ</span>

  <h5 style="left:415px;top:16px">Social Network</h5>
  <span class="soc" style="left:420px;top:42px"></span><span class="lnk" style="left:437px;top:40px">Live Chat</span>
  <span class="soc" style="left:420px;top:64px"></span><span class="lnk" style="left:437px;top:62px">Send Mail</span>
  <span class="soc" style="left:420px;top:86px"></span><span class="lnk" style="left:437px;top:84px">FAQ</span>

  <h5 style="left:540px;top:16px">Get Discount</h5>
</footer>
<div class="abs email">Email Address</div>
<div class="abs subscribe">SUBSCRIBE</div>
<div class="abs secure"><span class="secure-box"></span><div class="secure-text">secured by<b>SafeTill</b></div></div>

<div class="abs bottom">Copyrights @ 2014 The Loam Barrow. All rights reserved</div>

</body>
</html>
```